Wedding on the paradise

We are getting married in Koh Samui Thailand and need booklet/ concertina that contains the invitation, event program (Day 1 Sunset Cocktail Party, Day 2 Wedding Day, Day 4 Sunset Cruise) and information about the island of Koh Samui.

Also looking for the Wedding Day Program, Menu and card containing guest names.

Below is the link to my favorite invitation and would like similar outcome.

http://www.lumeradesigns.com/wedding/couture.php?c=styles&s=destination&p=tova_marsh

We have international guests and therefore require text in Mongolian and English.

Industry/Entity Type

Wedding

Colors
cedeec

```html
<!DOCTYPE html>
<html lang="en">
<head>
<meta charset="utf-8">
<title>Nalin &amp; Tomas – Wedding Booklet</title>
<link rel="stylesheet" href="https://fonts.googleapis.com/css2?family=Great+Vibes&family=Tinos&display=swap">
<style>
  :root {
    --page: #ffffff;
    --paper: #eef7fa;
    --paper-edge: #e4f1f6;
    --frame: #111111;
    --ink-soft: #86d0f2;
    --ink-pale: #c9ecfb;
    --ink-script: #1424e6;
    --art-main: #a9def5;
    --art-light: #d6f0fb;
  }
  * { margin: 0; padding: 0; box-sizing: border-box; }
  html, body { width: 900px; height: 1200px; overflow: hidden; background: var(--page); }
  body { position: relative; font-family: "Tinos", "Times New Roman", serif; color: var(--ink-soft); }

  .spread {
    position: absolute; left: 70px; width: 768px;
    border: 2px solid var(--frame);
    background: radial-gradient(ellipse at 40% 30%, var(--paper) 0%, var(--paper-edge) 100%);
  }
  .spread--front { top: 15px; height: 578px; }
  .spread--back { top: 606px; height: 579px; }

  .el { position: absolute; text-align: center; }
  .title { font-size: 30px; letter-spacing: 0.5px; line-height: 1; }
  .title--large { font-size: 38px; }
  .body { font-size: 12px; line-height: 15px; }
  .script { font-family: "Great Vibes", cursive; color: var(--ink-script); line-height: 1; white-space: nowrap; }
  .subline { font-size: 15px; color: #d3efff; }

  .rule { position: absolute; height: 0; border-top: 1px solid var(--ink-soft); }
  .rule--dashed { border-top: 1px dashed var(--ink-soft); }

  .art { position: absolute; }
  .monogram { border-radius: 50%; background: radial-gradient(circle, var(--art-light) 30%, var(--art-main) 100%); opacity: 0.85; }
  .tree { border-radius: 50% 50% 10% 10%; background: radial-gradient(ellipse at 50% 35%, var(--art-main), var(--art-light) 70%, transparent 100%); }
  .dancers { background: linear-gradient(180deg, var(--art-light), var(--art-main)); opacity: 0.75; }
  .boat { background: linear-gradient(180deg, transparent, var(--art-light) 30%, var(--art-main)); opacity: 0.6; }
  .divider-ornament { background: var(--art-main); height: 3px; border-radius: 2px; }

  .info { position: absolute; left: 406px; top: 172px; width: 340px; }
  .info__item { margin-bottom: 14px; }
  .info__label { font-size: 15px; line-height: 18px; }
  .info__text { font-size: 12px; line-height: 15px; margin-top: 4px; text-indent: 36px; }
  .info__text--tight { text-indent: 0; padding-left: 34px; }
</style>
</head>
<body>

<section class="spread spread--front">
  <h1 class="el title" style="left:0; width:370px; top:88px;">INVITATION</h1>
  <p class="el body" style="left:0; width:370px; top:270px;">Together with their parents Nalin &amp; Tomas would like to invite</p>
  <div class="rule rule--dashed" style="left:58px; width:268px; top:322px;"></div>
  <p class="el body" style="left:0; width:370px; top:345px;">
    to celebrate their union.<br>Saturday, December 13, 2014<br>Ceremony at four o’clock in the afternoon<br>Baan Selara Lipa Noi Koh Samui
  </p>

  <div class="art monogram" role="img" aria-label="Couple monogram inside a sun-ray ornament" style="left:545px; top:33px; width:66px; height:66px;"></div>
  <h2 class="el title" style="left:428px; width:300px; top:135px;">WELCOME</h2>
  <p class="el body" style="left:426px; width:306px; top:179px;">
    To our family and friends, it means the world to us to have you here. Thank you for the support, love and laughter you have contributed to our lives. We hope you enjoy and relax your time in Koh Samui. Here is the weekend full of LOVE.
  </p>
  <p class="el script" style="left:428px; width:300px; top:270px; font-size:44px;">Nalin &amp; Tomas</p>
  <div class="art tree" role="img" aria-label="Faint illustration of a lone tree" style="left:540px; top:350px; width:80px; height:68px;"></div>
  <h3 class="el script" style="left:428px; width:300px; top:422px; font-size:44px; font-weight:400;">Sunset Cocktail</h3>
  <p class="el body" style="left:418px; width:320px; top:479px;">At the first day with us, we relax, sip cocktail by the pool and enjoy beautiful Koh Samui.</p>
  <p class="el body" style="left:418px; width:320px; top:523px;">Baan Selara 3pm</p>
</section>

<section class="spread spread--back">
  <div class="art dancers" role="img" aria-label="Faint illustration of a row of Thai classical dancers" style="left:52px; top:48px; width:294px; height:102px;"></div>
  <div class="rule" style="left:18px; width:350px; top:151px;"></div>
  <h3 class="el script" style="left:40px; width:320px; top:178px; font-size:46px; font-weight:400;">Wedding Day</h3>
  <p class="el body" style="left:20px; width:360px; top:240px;">Ceremony at 5 pm followed by celebration<br>Transportation from Bo Phut departing from 3.45 pm</p>
  <div class="art divider-ornament" role="img" aria-label="Small decorative divider" style="left:154px; top:287px; width:100px;"></div>
  <div class="rule" style="left:18px; width:350px; top:305px;"></div>
  <h3 class="el script" style="left:100px; width:300px; top:346px; font-size:44px; font-weight:400;">Sunset Cruise</h3>
  <p class="el subline" style="left:100px; width:300px; top:401px;">Post Wedding Chillax</p>
  <div class="art boat" role="img" aria-label="Faint illustration of a man on a traditional sailing boat" style="left:20px; top:400px; width:150px; height:170px;"></div>

  <h2 class="el title title--large" style="left:426px; width:300px; top:68px;">INFO</h2>
  <div class="info">
    <div class="info__item"><p class="info__label">Dress</p><p class="info__text info__text--tight">Smart Casual</p></div>
    <div class="info__item"><p class="info__label">Getting there</p><p class="info__text">There will be a shuttle bus from Bo Phut to the ceremony. Please let us know if you are interested</p></div>
    <div class="info__item"><p class="info__label">Gifts</p><p class="info__text">Your presence at our wedding is the greatest gift of all.</p></div>
    <div class="info__item"><p class="info__label">Champagne/Wine</p><p class="info__text">Koh Samui is a tropical island where a champagne and wine can be dear. For your enjoyment and ease for the pockets we advise our guests to bring a bottle of champagne or/and wine with you</p></div>
    <div class="info__item"><p class="info__label">Our website</p><p class="info__text">Please check for any updates or changes in our wedding site nalin-tomasnearlyweds.com</p></div>
  </div>
</section>

</body>
</html>
```